Carpentry and Building Business Card

I'm looking for a business card that is minimalistic and that incorporates the theme of my Velmi logo.
On one side I'd like the VELMI logo with my details on the other side.
Double sided with curved edges

Target Market(s)

Construction / renovation
Adults

Industry/Entity Type

Tradesman

Contact Information for Business Card

Logo on one side, details on the other

Colors

Designer to choose only greyscale colors for use in the design.

Requirements
Must have
• Niko Barlettis
VELMI CONSTRUCT
Carpentry & Building Services
0412385726
Velmiconstruct@brindlemail.com
Lic No. 618243D
Nice to have
• Fb and insta icons. @velmiconstruct
Should not have
• No hammer or tool icons please.

No address line.

```html
<!DOCTYPE html>
<html lang="en">
<head>
<meta charset="utf-8">
<title>Velmi Construct – Business Card</title>
<link href="https://fonts.googleapis.com/css2?family=Montserrat:wght@500&family=Lato:wght@700&family=Arimo:wght@400&display=swap" rel="stylesheet">
<style>
  :root {
    --bg-light: #b9b9b9;
    --bg-dark: #8a8a8a;
    --card-dark: #231f20;
    --card-light: #ffffff;
    --ink: #231f20;
    --ink-soft: #e2e2e2;
    --accent: #f0922f;
    --rule: #6d6d6d;
  }
  * { margin: 0; padding: 0; box-sizing: border-box; }
  html, body { width: 1200px; height: 1200px; overflow: hidden; }
  body {
    position: relative;
    background: radial-gradient(circle at 50% 55%, var(--bg-light) 0%, var(--bg-dark) 100%);
  }
  .card {
    position: absolute;
    border-radius: 16px;
    overflow: hidden;
  }
  .card--front {
    left: 202px; top: 305px; width: 368px; height: 592px;
    background: var(--card-dark);
  }
  .card--back {
    left: 599px; top: 303px; width: 364px; height: 593px;
    background: var(--card-light);
  }
  .brand {
    position: absolute;
    display: flex;
    align-items: center;
  }
  .brand__mark {
    border: 2px solid var(--accent);
    flex: none;
  }
  .brand__name {
    font-family: "Montserrat", sans-serif;
    font-weight: 500;
    letter-spacing: 0.33em;
    line-height: 1;
  }
  .card--front .brand { left: 45px; top: 277px; }
  .card--front .brand__mark { width: 62px; height: 62px; margin-right: 17px; }
  .card--front .brand__name { font-size: 32px; color: var(--ink-soft); }

  .card--back .brand { left: 37px; top: 144px; }
  .card--back .brand__mark { width: 65px; height: 65px; margin-right: 16px; }
  .card--back .brand__name { font-size: 32px; color: var(--ink); }

  .social {
    position: absolute;
    left: 0; right: 0; top: 528px;
    display: flex; justify-content: center; align-items: center;
    font-family: "Arimo", sans-serif;
    font-size: 18px;
    color: var(--ink-soft);
  }
  .social__icon {
    width: 22px; height: 22px;
    border-radius: 4px;
    background: var(--accent);
    margin-right: 8px;
  }

  .details {
    position: absolute;
    left: 0; right: 0; top: 380px;
    text-align: center;
    font-family: "Arimo", sans-serif;
    color: var(--ink);
  }
  .details__name {
    font-family: "Lato", sans-serif;
    font-weight: 700;
    font-size: 22px;
    color: var(--accent);
    line-height: 1;
  }
  .details__role { font-size: 17.5px; margin-top: 6px; letter-spacing: 0.01em; }
  .details__rule {
    width: 92px; height: 1px; background: var(--rule);
    margin: 12px auto 0;
  }
  .details__licence { font-size: 17px; margin-top: 13px; }
  .details__licence span { color: var(--accent); }
  .details__rule--second { margin-top: 14px; }
  .details__phone { font-size: 22px; margin-top: 15px; }
  .details__email { font-size: 15.5px; margin-top: 6px; }
</style>
</head>
<body>
  <section class="card card--front">
    <div class="brand">
      <div class="brand__mark"></div>
      <span class="brand__name">VELMI.</span>
    </div>
    <div class="social">
      <span class="social__icon"></span>
      <span>@velmiconstruct</span>
    </div>
  </section>

  <section class="card card--back">
    <div class="brand">
      <div class="brand__mark"></div>
      <span class="brand__name">VELMI.</span>
    </div>
    <div class="details">
      <p class="details__name">NIKO BARLETTIS</p>
      <p class="details__role">CARPENTRY &amp; BUILDING SERVICES</p>
      <div class="details__rule"></div>
      <p class="details__licence"><span>LIC NO</span>. 618243D</p>
      <div class="details__rule details__rule--second"></div>
      <p class="details__phone">0412385726</p>
      <p class="details__email">VELMICONSTRUCT@BRINDLEMAIL.COM</p>
    </div>
  </section>
</body>
</html>
```